RPN FORMED

building services
decks
pergola
renovation
extensions
general building

Target Market(s)

middle to upper class

Industry/Entity Type

building

Contact Information for Business Card

my details 0438917264 tkbarrow47@mailvora.com BLD581047

Font styles to use
Serif

Colors
00AB8E
00BBA5
67D7C9
C6EFE9
E9F9F6

Requirements
Must have
• logo on the front and details on the back
Nice to have
• sharp and clean lines

```html
<!DOCTYPE html>
<html lang="en">
<head>
<meta charset="UTF-8">
<title>RPN FORMED – Business Card</title>
<link href="https://fonts.googleapis.com/css2?family=Tinos:wght@400;700&family=Montserrat:wght@600&display=swap" rel="stylesheet">
<style>
  :root {
    --bg: #c9c9c9;
    --card-dark: #141414;
    --card-light: #ffffff;
    --ink: #1e1e1e;
    --ink-soft: #3a3a3a;
    --rule: #b8b8b8;
    --teal: #00bba5;
    --teal-light: #67d7c9;
    --white: #ffffff;
  }
  * { box-sizing: border-box; margin: 0; padding: 0; }
  html, body {
    width: 1200px; height: 852px; overflow: hidden;
    background: var(--bg);
  }
  .stage { position: relative; width: 1200px; height: 852px; }

  .card {
    position: absolute;
    width: 540px; height: 310px;
    border-radius: 20px;
    box-shadow: 0 6px 18px rgba(0,0,0,0.18);
  }

  /* Front: logo side */
  .card-front {
    left: 80px; top: 110px;
    background: var(--card-dark);
  }
  .card-front .brand {
    position: absolute; right: 34px; bottom: 36px;
    display: flex; align-items: center; gap: 10px;
    font-family: "Tinos", serif; font-weight: 700;
    font-size: 26px; letter-spacing: 1px;
    color: var(--white);
  }
  .brand-dot {
    width: 10px; height: 10px; border-radius: 50%;
    background: var(--teal-light);
  }

  /* Back: details side */
  .card-back {
    left: 580px; top: 432px;
    background: var(--card-light);
    font-family: "Tinos", serif;
    color: var(--ink);
  }
  .card-back .brand {
    position: absolute; left: 40px; top: 108px;
    display: flex; align-items: center; gap: 10px;
    font-weight: 700; font-size: 30px; letter-spacing: 1px;
    color: var(--ink);
  }
  .divider {
    position: absolute; left: 262px; top: 64px;
    width: 1px; height: 96px; background: var(--rule);
  }
  .details { position: absolute; left: 280px; top: 60px; }
  .person-name { font-size: 19px; letter-spacing: 1px; }
  .person-role {
    font-family: "Montserrat", sans-serif; font-weight: 600;
    font-size: 10px; letter-spacing: 1.5px; color: var(--teal);
    margin: 3px 0 6px 14px;
  }
  .contact-list { list-style: none; margin-left: 14px; font-size: 13px; line-height: 18px; color: var(--ink-soft); }
  .contact-list .label { color: var(--teal); }

  .services {
    position: absolute; left: 0; right: 0; bottom: 46px;
    text-align: center; font-size: 14px; letter-spacing: 1.2px;
    line-height: 22px; color: var(--ink-soft);
  }
  .services .sep {
    display: inline-block; width: 5px; height: 5px; border-radius: 50%;
    background: var(--teal); vertical-align: middle; margin: 0 6px;
  }
</style>
</head>
<body>
<main class="stage">
  <section class="card card-front" aria-label="Card front">
    <div class="brand"><span>RPN FORMED</span><span class="brand-dot"></span></div>
  </section>

  <section class="card card-back" aria-label="Card back">
    <div class="brand"><span>RPN FORMED</span><span class="brand-dot"></span></div>
    <div class="divider"></div>
    <div class="details">
      <p class="person-name">KEIRAN BARROW</p>
      <p class="person-role">OWNER</p>
      <ul class="contact-list">
        <li><span class="label">P:</span> 0438917264</li>
        <li><span class="label">E:</span> tkbarrow47@mailvora.com</li>
        <li><span class="label">L:</span> BLD581047</li>
      </ul>
    </div>
    <p class="services">
      BUILDING SERVICES<span class="sep"></span>DECKS<span class="sep"></span>PERGOLA<span class="sep"></span>RENOVATION<br>
      EXTENSIONS<span class="sep"></span>GENERAL BUILDING
    </p>
  </section>
</main>
</body>
</html>
```